MCP phase 1 web design

Meridale Capital Partners Ltd (MCP) is a challenger business to the traditional leasing market. We look for solutions to complex problems involving the funding of capital equipment within an office environment and then build documentation around the solution. We recently created a brief for a logo and successfully completed that assignment. We now need to create our first web site which is simply intended to be informative. To help interested designers we have attached a detailed brief that is broken into three sections. The first explains how we see the site developing over time from something quite straightforward initially to a full transaction capability. Whoever wins this competition will be expected to work with us into the future to help develop the site. Section 2 gives you a view about our likes and dislikes by reviewing some existing sites. Section 3 gives you the structure and content of the site based upon our likes and dislikes. We are by no means committed to the structure and if you believe it can be presented in a better way then please use your design. The text is fixed as content. The images to appear can be anything from photographs to line drawings again entirely at the designers whim. Currently we have a home page plus 5 subsidiary pages. A few things to help you:
1. The logo is fixed and should be amongst the downloads.
2. The colours we have are corporate and should be used.
3. The typeface we use within the business is "Verdana"
Good luck.

Industry/Entity Type

Business

```html
<!DOCTYPE html>
<html lang="en">
<head>
<meta charset="utf-8">
<title>Meridale Capital Partners Ltd</title>
<link rel="stylesheet" href="https://fonts.googleapis.com/css2?family=Lato:ital,wght@0,400;0,700;1,400&family=Rubik:wght@300;400&family=Roboto+Condensed:wght@400&display=swap">
<style>
:root{
  --blue:#1f73c4;
  --blue-dark:#1a5fa6;
  --ink:#333;
  --muted:#555;
  --line:#d9d9d9;
  --panel:#ebedf0;
  --footer:#000;
  --social:#4a4a4a;
}
*{box-sizing:border-box;margin:0;padding:0}
html,body{width:833px;height:1200px;overflow:hidden;background:#fff}
body{position:relative;font-family:"Lato",sans-serif;color:var(--ink)}
.abs{position:absolute}
.h{font-family:"Rubik",sans-serif;font-weight:300}

/* top bar */
.topbar{left:0;top:0;width:833px;height:24px;border-bottom:1px solid #e3e3e3}
.call{left:470px;top:6px;font-size:10.5px;color:#555;display:flex;align-items:center;gap:4px}
.call b{color:var(--blue);font-weight:400}
.topsoc{top:4px;width:16px;height:16px;border-radius:50%;background:var(--blue)}
.brand{font-family:"Rubik",sans-serif;font-weight:300;color:var(--blue);letter-spacing:.5px;white-space:nowrap}

/* nav */
.nav{top:47px;height:25px;font-family:"Rubik",sans-serif;font-size:11px;color:#444;display:flex;align-items:center}
.nav.active{background:var(--blue);color:#fff;padding:0 9px}

/* hero */
.hero-photo{left:0;top:94px;width:546px;height:325px;background:linear-gradient(100deg,#e9eaec 0%,#c9ccd0 35%,#6f757d 60%,#d6d8db 85%,#b9bcc0 100%)}
.hero-panel{left:546px;top:94px;width:287px;height:325px;background:linear-gradient(160deg,#3a86d6 0%,#2a74c4 55%,#1c5ea8 100%)}
.hero-text{left:558px;top:136px;width:186px;color:#fff;font-size:12px;line-height:17.6px}
.hero-text p+p{margin-top:11px}
.caption{left:96px;top:392px;height:27px;background:rgba(0,0,0,.75);color:#fff;font-family:"Roboto Condensed",sans-serif;font-size:12.5px;line-height:27px;padding:0 14px 0 18px;white-space:nowrap}
.dot{width:6px;height:6px;border-radius:50%;top:403px;background:#555}

/* services */
.services{left:0;top:419px;width:833px;height:173px;background:linear-gradient(#eef0f2,#fff 40%,#fff 60%,#eceef1)}
.card{top:450px;width:211px;height:118px;background:#fff;border:1px solid #e2e4e7;box-shadow:0 4px 3px -2px rgba(0,0,0,.25)}
.card h3{position:absolute;left:8px;top:9px;font-family:"Rubik",sans-serif;font-weight:300;font-size:14px;color:var(--blue);white-space:nowrap}
.card .icon{position:absolute;left:8px;top:38px}
.card p{position:absolute;left:49px;top:35px;width:152px;font-size:9px;line-height:13.6px;color:#333}
.card .more{position:absolute;right:-1px;bottom:-1px;width:70px;height:18px;background:#3a3a3a;color:#fff;font-size:8px;font-weight:700;line-height:18px;text-align:right;padding-right:8px;clip-path:polygon(12px 0,100% 0,100% 100%,0 100%)}

/* welcome */
.welcome-h{left:98px;top:626px;font-size:19px;color:#444;display:flex;align-items:baseline;gap:8px}
.rule{height:1px;background:var(--line)}
.lead{left:98px;top:673px;font-size:9px;font-weight:700}
.body{left:98px;top:691px;width:320px;font-size:9.2px;line-height:14.5px;color:#444}
.btn{background:linear-gradient(#3b8ad8,#1f68b5);color:#fff;border-radius:2px;font-size:8.5px;font-weight:700;display:flex;align-items:center;justify-content:center;box-shadow:0 1px 2px rgba(0,0,0,.3)}
.video{left:436px;top:632px;width:299px;height:146px;background:linear-gradient(110deg,#8fa6bd 0%,#c8d4de 40%,#e4e9ee 65%,#9aa9b7 100%)}
.controls{left:436px;top:778px;width:299px;height:27px;background:#111;color:#fff;font-size:10px}

/* calculators & stories */
.panel{left:0;top:836px;width:833px;height:234px;background:var(--panel)}
.sec-h{top:860px;font-size:19px;color:var(--blue);display:flex;align-items:center;gap:10px}
.lbl{left:101px;font-size:8.6px;color:#333}
.field{left:191px;width:195px;height:17px;background:#fff;border:1px solid #d3d5d8;font-size:8px;color:#555;padding-left:5px;line-height:15px}
.slider{left:191px;width:195px;height:2px;background:#bfc2c6}
.knob{width:7px;height:7px;border-radius:50%;background:#888;border:1px solid #666}
.sum{left:101px;font-size:8.6px}
.sum b{font-size:10px;font-weight:700}
.story{left:446px;width:287px;background:#fff;border:1px solid #e0e2e5}
.story .avatar{position:absolute;left:8px;top:6px;width:47px;height:45px;background:linear-gradient(#c9d7e3,#7d8fa2)}
.story q{position:absolute;left:62px;top:10px;width:218px;font-style:italic;font-size:8.4px;line-height:14.6px;color:#333;quotes:none}
.story q::before{content:"\201C";color:#bbb;font-size:14px;font-style:normal;margin-right:4px;vertical-align:-3px}
.story:after{content:"";position:absolute;left:12px;bottom:-8px;border-left:16px solid #fff;border-bottom:8px solid transparent}
.byline{left:496px;font-size:8px}
.byline b{font-weight:700;margin-right:6px}
.byline i{color:#444}

/* footer */
.footer{left:0;top:1070px;width:833px;height:130px;background:var(--footer);color:#fff}
.fsoc{top:1111px;width:19px;height:19px;border-radius:50%;background:var(--social)}
</style>
</head>
<body>

<!-- top bar -->
<div class="abs topbar"></div>
<div class="abs call">
  <svg width="12" height="12" viewBox="0 0 12 12"><circle cx="6" cy="6" r="5.3" fill="none" stroke="#777"/><path d="M4 3.5c0 2.5 1.5 4.5 4 5l.6-1.2-1.3-.7-.6.7C5.8 6.8 5.2 6 5 5.2l.7-.6L5 3.2z" fill="#777"/></svg>
  Call Us: <b>555-014-2290</b>
</div>
<div class="abs topsoc" style="left:618px">
  <svg width="16" height="16" viewBox="0 0 16 16"><circle cx="7" cy="7" r="3.3" fill="none" stroke="#fff" stroke-width="1.5"/><path d="M9.4 9.4 12 12" stroke="#fff" stroke-width="1.8"/></svg>
</div>
<div class="abs topsoc" style="left:640px;background:#3b5a98"></div>
<div class="abs topsoc" style="left:663px;background:#2aa3e0"></div>
<div class="abs topsoc" style="left:686px;background:#1a78b5"></div>
<div class="abs topsoc" style="left:708px;background:#e0463a"></div>

<!-- header -->
<div class="abs brand" style="left:98px;top:48px;font-size:19px">MCP Meridale Capital Partners Ltd</div>
<div class="abs nav active" style="left:450px">Home</div>
<div class="abs nav" style="left:514px">Why Meridale ⌄</div>
<div class="abs nav" style="left:615px">Solutions ⌄</div>
<div class="abs nav" style="left:687px">Contact ⌄</div>

<!-- hero -->
<div class="abs hero-photo" role="img" aria-label="Photo of smiling business colleagues in an office"></div>
<div class="abs hero-panel" role="img" aria-label="Blue-tinted photo of a businessman walking up steps"></div>
<div class="abs hero-text">
  <p>We provide "<b>Sales Aid Finance</b>" through <b>MERIDALE</b> financial and contract solutions. Specialising in the Print and Technology markets, we offer Value Added Resellers (VARs) a range of innovative, cost effective, value added contract and finance options to enhance their sales.</p>
  <p>Our solutions are fully financed and we are totally independent from any VAR, technology provider or traditional finance house.</p>
</div>
<div class="abs dot" style="left:68px;background:var(--blue)"></div>
<div class="abs dot" style="left:81px"></div>
<div class="abs caption">We are a Challenger Business to the Traditional Leasing Market</div>
<div class="abs dot" style="left:458px"></div>
<div class="abs dot" style="left:472px"></div>

<!-- services -->
<div class="abs services"></div>
<div class="abs card" style="left:90px">
  <h3>Managed Services Solutions</h3>
  <svg class="icon" width="34" height="34" viewBox="0 0 34 34"><circle cx="12" cy="20" r="9" fill="#8a8a8a"/><circle cx="12" cy="20" r="3.5" fill="#fff"/><circle cx="25" cy="8" r="6" fill="#9a9a9a"/><circle cx="25" cy="8" r="2.2" fill="#fff"/></svg>
  <p>Large enterprises, as well as SMEs, non-for profit and most Public Sector organisations, ask for flexibility as a key requirement for...</p>
  <div class="more">Read more »</div>
</div>
<div class="abs card" style="left:310px">
  <h3>Public Sector Solutions</h3>
  <svg class="icon" width="38" height="30" viewBox="0 0 38 30"><circle cx="19" cy="8" r="6" fill="#8a8a8a"/><path d="M8 26c0-8 5-11 11-11s11 3 11 11z" fill="#8a8a8a"/><circle cx="7" cy="11" r="4.5" fill="#a0a0a0"/><path d="M0 27c0-6 3-9 7-9 2 0 3 1 3 1-2 2-3 5-3 8z" fill="#a0a0a0"/><circle cx="31" cy="11" r="4.5" fill="#a0a0a0"/><path d="M38 27c0-6-3-9-7-9-2 0-3 1-3 1 2 2 3 5 3 8z" fill="#a0a0a0"/></svg>
  <p>Most public sector bodies increa-singly require contract flexibility. In particular, some large tender frameworks contain clauses that ...</p>
  <div class="more">Read more »</div>
</div>
<div class="abs card" style="left:531px">
  <h3>Education Solutions</h3>
  <svg class="icon" width="36" height="30" viewBox="0 0 36 30"><path d="M18 2 35 10 18 18 1 10z" fill="#8a8a8a"/><path d="M8 14v8c3 3 17 3 20 0v-8l-10 5z" fill="#9a9a9a"/><path d="M32 11v10" stroke="#8a8a8a" stroke-width="1.5"/></svg>
  <p>Using the right type of financial product is essential for technology projects in the Education sector. We understand the ...</p>
  <div class="more">Read more »</div>
</div>

<!-- welcome -->
<div class="abs welcome-h h">Welcome To <span class="brand" style="font-size:16px">MCP Meridale</span></div>
<div class="abs rule" style="left:98px;top:659px;width:319px"></div>
<div class="abs lead">Lorem ipsum dolor sit amet, consectetuer adipiscing elit, sed diam</div>
<div class="abs body">Consectetuer adipiscing elit, sed diam nonummy nibh euismod tincidunt ut laoreet dolore ma aliqua erat volutpat. Ut wisi enim ad minim veniam, quis nostrud exerci tation ullamcorper suscipit lob nisl ut aliquip ex ea commodo consequat. Duis autem vel eum iriure dolor in hendrerit in vulputate esse molestie consequat, vel illum dolore eu feugiat nulla facilisis at vero eros et dolore te feugait nulla facilisi.</div>
<div class="abs btn" style="left:99px;top:786px;width:82px;height:23px">Read more »</div>

<div class="abs video" role="img" aria-label="Video still of a smiling businessman with colleagues behind him"></div>
<svg class="abs" style="left:570px;top:701px" width="30" height="30" viewBox="0 0 30 30"><circle cx="15" cy="15" r="14" fill="rgba(0,0,0,.45)"/><path d="M12 9v12l9-6z" fill="#fff"/></svg>
<div class="abs controls">
  <svg class="abs" style="left:10px;top:8px" width="10" height="11"><path d="M0 0v11l10-5.5z" fill="#fff"/></svg>
  <span class="abs" style="left:37px;top:7px">04:59</span>
  <div class="abs" style="left:70px;top:11px;width:140px;height:6px;border-radius:3px;background:#333"></div>
  <div class="abs" style="left:70px;top:11px;width:85px;height:6px;border-radius:3px;background:#555"></div>
  <div class="abs" style="left:151px;top:10px;width:8px;height:8px;border-radius:50%;background:#888"></div>
  <span class="abs" style="left:216px;top:7px">10:35</span>
  <svg class="abs" style="left:250px;top:7px" width="16" height="14"><path d="M0 4h4l5-4v14l-5-4H0z" fill="#fff"/><path d="M11 3c2 2 2 6 0 8" stroke="#fff" fill="none" stroke-width="1.3"/></svg>
  <svg class="abs" style="left:276px;top:6px" width="15" height="15"><path d="M1 1l13 13M1 1v5M1 1h5M14 14v-5M14 14H9" stroke="#fff" stroke-width="2" fill="none"/></svg>
</div>

<!-- calculators & stories -->
<div class="abs panel"></div>
<div class="abs sec-h h" style="left:101px">
  <svg width="18" height="20" viewBox="0 0 18 20"><rect x="1" y="1" width="16" height="18" rx="2" fill="none" stroke="#666" stroke-width="1.5"/><rect x="4" y="4" width="10" height="4" fill="#666"/><g fill="#666"><rect x="4" y="10" width="3" height="3"/><rect x="8" y="10" width="3" height="3"/><rect x="12" y="10" width="2" height="3"/><rect x="4" y="14" width="3" height="3"/><rect x="8" y="14" width="3" height="3"/><rect x="12" y="14" width="2" height="3"/></g></svg>
  Fee Calculators
</div>
<div class="abs rule" style="left:98px;top:891px;width:288px;background:#cfd2d6"></div>
<div class="abs" style="left:417px;top:860px;width:1px;height:188px;background:#cfd2d6"></div>

<div class="abs lbl" style="top:909px">Your revenue</div>
<div class="abs field" style="top:906px">$200k</div>
<div class="abs lbl" style="top:929px">Invoice Value</div>
<div class="abs slider" style="top:932px"></div>
<div class="abs knob" style="left:200px;top:929px"></div>
<div class="abs field" style="top:943px">$100,000</div>
<div class="abs lbl" style="top:967px">Time Outstanding</div>
<div class="abs slider" style="top:971px"></div>
<div class="abs knob" style="left:208px;top:968px"></div>
<div class="abs field" style="top:981px">30days</div>
<div class="abs sum" style="top:1008px">Transfered to you immediately: <b>$76,510</b></div>
<div class="abs sum" style="top:1031px">Total fees: <b>$4,490</b></div>
<div class="abs btn" style="left:304px;top:1023px;width:82px;height:23px;font-size:9.5px;font-weight:400">Apply Now</div>

<div class="abs sec-h h" style="left:453px">
  <svg width="16" height="19" viewBox="0 0 16 19"><circle cx="8" cy="5" r="4.5" fill="#666"/><path d="M0 19c0-6 3-9 8-9s8 3 8 9z" fill="#666"/></svg>
  Customer Stories
</div>
<div class="abs rule" style="left:446px;top:891px;width:288px;background:#cfd2d6"></div>

<div class="abs story" style="top:906px;height:56px">
  <div class="avatar" role="img" aria-label="Portrait photo of a customer"></div>
  <q>Consectetuer adipiscing elit, sed diam nonum nibh euismod tincidunt ut laoreet dolore aliqua er volutpat. Ut wisi enim ad minim veniam, nostrud.</q>
</div>
<div class="abs byline" style="top:967px"><b>Daniel Hartley</b><i>Marketing Manager - Company name</i></div>
<div class="abs story" style="top:984px;height:58px">
  <div class="avatar" role="img" aria-label="Portrait photo of a customer"></div>
  <q>Consectetuer adipiscing elit, sed diam nonum nibh euismod tincidunt ut laoreet dolore aliqua er volutpat. Ut wisi enim ad minim veniam, nostrud.</q>
</div>
<div class="abs byline" style="top:1046px"><b>Daniel Hartley</b><i>Marketing Manager - Company name</i></div>

<!-- footer -->
<div class="abs footer"></div>
<div class="abs" style="left:98px;top:1099px;color:#fff;font-size:9.5px;font-weight:700">Sign up for Newsletter</div>
<div class="abs" style="left:98px;top:1121px;width:123px;height:17px;background:#fff;font-size:8px;font-style:italic;color:#888;padding-left:7px;line-height:17px">Your Email Address</div>
<div class="abs" style="left:221px;top:1121px;width:63px;height:17px;background:#555;color:#fff;font-size:10px;line-height:17px;text-align:center">Subscribe</div>
<div class="abs brand" style="left:322px;top:1110px;color:#fff;font-size:17px">MCP Meridale</div>
<svg class="abs" style="left:572px;top:1096px" width="38" height="18" viewBox="0 0 38 18"><path d="M37 1 18 8l6 3zM37 1 24 11l1 6 3-4" fill="#fff"/><path d="M16 14c-5 2-10 2-15 0" stroke="#fff" stroke-dasharray="2 2" fill="none"/></svg>
<div class="abs" style="left:555px;top:1115px;color:#fff;font-size:9.5px;font-weight:700">Stay in touch</div>
<div class="abs fsoc" style="left:628px"></div>
<div class="abs fsoc" style="left:653px"></div>
<div class="abs fsoc" style="left:680px"></div>
<div class="abs fsoc" style="left:706px"></div>
<div class="abs" style="left:90px;top:1170px;width:651px;height:1px;background:#333"></div>
<div class="abs" style="left:0;top:1178px;width:833px;text-align:center;color:#ccc;font-size:8px">© 2014 Meridale Capital Partners Ltd. All Rights Reserved.</div>

</body>
</html>
```